Website For Custom Home Builder

-Very elegant and simple design as I am a high end custom home builder.
-I build homes $2 million to $10 million range so the website needs to reflect the level of home that I build.
-Attached are photos of homes I have built to use as well as my logo.
-I need final design to be in layered format so my local guy can edit if he needs to.

3 Page Design
1. HomePage:
-logo, some photos,
-“Building beautiful custom homes in Indianapolis for over 20 years”
2. AboutPage:
-Dean Morley has been building stunning custom homes in the Indianpolis area for over 20 years. As a small boutique building company we only build a handful of homes a year in order to offer our clients the personal attention that their homes deserve. It's this attention to detail that makes our client experience and final product something special and unique.
- family photo
3. ContactPage:
-office photo
-317-555-0192
-dean@dmbuildco.example
-415 North Larkwood Dr, Suite 310, Carmel IN 46099

Target Market(s)

Very high end clients looking to build $2 million to $10 million homes.

Industry/Entity Type

Residential high end custom home builder/construction

Coding

Coded - Design and coding required

Number of Pages Required

3 page

Requirements
Must have
• Very simple and elegant design that represents the high end homes that I build.
Nice to have
Should not have
• Should NOT have a lot of clutter or be a very busy page from a design perspective.

```html
<!DOCTYPE html>
<html lang="en">
<head>
<meta charset="utf-8">
<title>Dean Morley Custom Homes</title>
<link rel="stylesheet" href="https://fonts.googleapis.com/css2?family=Poppins:wght@300;400;500;600&display=swap">
<style>
:root{
  --ink:#2b2b2b;
  --muted:#4a4a4a;
  --brown:#8a4a16;
  --brown-dark:#3b2016;
  --brown-light:#b0662a;
  --line:#3a3a3a;
  --soft:#f8f8f8;
  --white:#ffffff;
}
*{margin:0;padding:0;box-sizing:border-box}
html,body{width:1200px;height:4139px;overflow:hidden}
body{font-family:"Poppins",sans-serif;color:var(--ink);background:var(--white);position:relative}
.abs{position:absolute}
.site-header{position:absolute;left:0;top:0;width:1200px;height:128px;background:var(--white)}
.brand{position:absolute;left:90px;top:44px;display:flex;align-items:center;gap:14px}
.brand-mark{width:28px;height:28px;border:3px solid var(--brown)}
.brand-name{font-size:28px;font-weight:400;color:var(--brown-dark);letter-spacing:.5px}
.main-nav a{position:absolute;top:57px;font-size:14px;color:var(--ink);text-decoration:none;letter-spacing:.3px}
.hero{position:absolute;left:0;top:128px;width:1200px;height:694px;background:linear-gradient(180deg,#7d6a55 0%,#a9835a 30%,#d8a258 55%,#a9876a 72%,#2c5c94 88%,#1e4e8c 100%)}
.hero h1{position:absolute;left:0;top:505px;width:1200px;text-align:center;color:var(--white);font-weight:500;font-size:40px;line-height:50px}
.dots{position:absolute;display:flex;gap:10px}
.dots span{width:12px;height:12px;border-radius:50%;background:rgba(255,255,255,.5)}
.dots span.on{background:var(--white)}
.about h2{position:absolute;left:81px;top:1040px;font-size:39px;font-weight:500;color:var(--ink);letter-spacing:.5px}
.rule{position:absolute;height:1px;background:var(--line)}
.about p{position:absolute;left:81px;top:1172px;width:420px;font-size:15px;line-height:25.7px;text-align:justify;color:var(--muted);font-weight:300}
.photo{position:absolute}
.frame{position:absolute;border:2px solid var(--line)}
.frame.tl{border-right:none;border-bottom:none}
.gallery-band{position:absolute;left:0;top:1620px;width:1200px;height:1303px;background:var(--soft)}
.gallery h2{position:absolute;left:0;top:1690px;width:1200px;text-align:center;font-size:39px;font-weight:500}
.g-dots span{width:16px;height:16px;background:#b99176}
.g-dots span.on{background:#6b3410}
.contact-bg{position:absolute;left:0;top:2923px;width:670px;height:792px;background:linear-gradient(90deg,#efefef,#f6f6f6)}
.contact h2{position:absolute;left:772px;top:3155px;font-size:40px;font-weight:600;color:#3a3a3a}
.contact-item{position:absolute;left:772px;display:flex;align-items:center;gap:22px;font-size:17px;color:var(--muted);line-height:22px}
.contact-item svg{flex:none}
.site-footer{position:absolute;left:0;top:3715px;width:1200px;height:424px;background:linear-gradient(110deg,#a2541a 0%,#7a3d15 45%,#3a1f15 100%)}
.footer-brand{position:absolute;left:0;top:110px;width:1200px;text-align:center;color:var(--white);font-size:32px;font-weight:400;letter-spacing:.5px}
.footer-nav a{position:absolute;top:236px;color:var(--white);font-size:14px;text-decoration:none}
.footer-sep{position:absolute;top:220px;width:1px;height:52px;background:rgba(255,255,255,.8)}
.copyright{position:absolute;left:92px;top:362px;color:var(--white);font-size:15px}
.social{position:absolute;top:354px;left:956px;display:flex;gap:9px}
.social span{width:35px;height:35px;border:1.5px solid var(--white);border-radius:50%}
</style>
</head>
<body>

<header class="site-header">
  <div class="brand"><span class="brand-mark"></span><span class="brand-name">Dean Morley</span></div>
  <nav class="main-nav">
    <a href="#" style="left:736px">HOME</a>
    <a href="#" style="left:868px">ABOUT US</a>
    <a href="#" style="left:1013px">CONTACT US</a>
  </nav>
</header>

<section class="hero" role="img" aria-label="Evening view of a stone custom home with lit patio, swings and pool">
  <h1>BUILDING BEAUTIFUL CUSTOM HOMES<br>IN INDIANAPOLIS FOR OVER 20 YEARS</h1>
  <div class="dots" style="left:530px;top:637px"><span></span><span></span><span></span><span class="on"></span><span></span><span></span></div>
</section>

<section class="about">
  <h2>ABOUT US</h2>
  <div class="rule" style="left:81px;top:1118px;width:66px"></div>
  <p>Dean Morley has been building stunning custom homes in the Indianpolis area for over 20 years. As a small boutique building company we only build a handful of homes a year in order to offer our clients the personal attention that their homes deserve. It's this attention to detail that makes our client experience and final product something special and unique.</p>
  <div class="frame" style="left:622px;top:1064px;width:513px;height:444px"></div>
  <div class="photo" role="img" aria-label="Stone and timber custom home exterior at dusk" style="left:572px;top:1021px;width:509px;height:442px;background:linear-gradient(180deg,#8a8a82 0%,#5a554d 30%,#c9b9a0 55%,#8c6a3e 80%,#3e4a2c 100%);border:1px solid #8a6a4a"></div>
</section>

<div class="gallery-band"></div>
<section class="gallery">
  <h2>GALLERY</h2>
  <div class="rule" style="left:567px;top:1764px;width:66px"></div>

  <div class="frame tl" style="left:80px;top:1807px;width:302px;height:305px"></div>
  <div class="photo" role="img" aria-label="Basement bar with screens and stools" style="left:100px;top:1826px;width:300px;height:306px;background:linear-gradient(180deg,#dcdcdc,#8b6a52 55%,#4a3528)"></div>

  <div class="frame tl" style="left:442px;top:1895px;width:302px;height:305px"></div>
  <div class="photo" role="img" aria-label="Bright living room with stone fireplace" style="left:462px;top:1913px;width:300px;height:306px;background:linear-gradient(180deg,#eeeeee,#c8c4bc 55%,#9e9890)"></div>

  <div class="frame tl" style="left:798px;top:2048px;width:302px;height:305px"></div>
  <div class="photo" role="img" aria-label="Wet bar with wood shelving and tall windows" style="left:819px;top:2067px;width:300px;height:306px;background:linear-gradient(90deg,#8a5a34,#d8d4cc 40%,#d8d4cc 60%,#8a5a34)"></div>

  <div class="frame tl" style="left:90px;top:2202px;width:302px;height:305px"></div>
  <div class="photo" role="img" aria-label="Oak staircase with glass railing" style="left:111px;top:2221px;width:300px;height:306px;background:linear-gradient(135deg,#6a5038,#c79a64 45%,#e2e2e0)"></div>

  <div class="frame tl" style="left:453px;top:2297px;width:302px;height:305px"></div>
  <div class="photo" role="img" aria-label="Basement bar with island seating" style="left:472px;top:2314px;width:300px;height:306px;background:linear-gradient(180deg,#e4e4e4,#6d5140 55%,#cfcfcf)"></div>

  <div class="frame tl" style="left:813px;top:2441px;width:302px;height:305px"></div>
  <div class="photo" role="img" aria-label="Dining area with live edge table" style="left:834px;top:2459px;width:300px;height:306px;background:linear-gradient(90deg,#7a8c6a,#e8e8e6 40%,#8a6a4c)"></div>

  <div class="dots g-dots" style="left:510px;top:2774px;gap:7px"><span></span><span></span><span></span><span></span><span class="on"></span><span></span></div>
</section>

<div class="contact-bg" role="img" aria-label="Faded view of a staircase interior"></div>
<section class="contact">
  <div class="frame" style="left:120px;top:3066px;width:475px;height:464px"></div>
  <div class="photo" role="img" aria-label="Light oak staircase with black metal railing" style="left:148px;top:3098px;width:477px;height:466px;background:linear-gradient(135deg,#ececea 0%,#d4b088 45%,#b98a58 70%,#e2e2e0 100%)"></div>

  <h2>Contact Us</h2>
  <div class="rule" style="left:772px;top:3228px;width:100px;background:var(--brown)"></div>

  <div class="contact-item" style="top:3300px">
    <svg width="44" height="44" viewBox="0 0 44 44"><path d="M22 2 42 16V42H2V16Z" fill="#8a4a16"/><path d="M22 14a7 7 0 0 0-7 7c0 5 7 12 7 12s7-7 7-12a7 7 0 0 0-7-7zm0 9.5a2.5 2.5 0 1 1 0-5 2.5 2.5 0 0 1 0 5z" fill="#fff"/></svg>
    <span>415 North Larkwood Dr,<br>Suite 310, Carmel IN 46099</span>
  </div>
  <div class="contact-item" style="top:3380px">
    <svg width="44" height="44" viewBox="0 0 44 44"><path d="M22 2 42 16V42H2V16Z" fill="#8a4a16"/><rect x="12" y="20" width="20" height="14" fill="#fff"/><path d="M12 20l10 8 10-8" fill="none" stroke="#8a4a16" stroke-width="1.6"/></svg>
    <span>dean@dmbuildco.example</span>
  </div>
  <div class="contact-item" style="top:3462px">
    <svg width="44" height="44" viewBox="0 0 44 44"><path d="M22 2 42 16V42H2V16Z" fill="#8a4a16"/><path d="M16 18c1-1 2-1 3 0l2 3c.5 1 0 2-1 2.5 1 2 2.5 3.5 4.5 4.5.5-1 1.5-1.5 2.5-1l3 2c1 1 1 2 0 3-2 2-5 1.5-8-1s-6-6-7-9c-.5-2 0-3 1-4z" fill="#fff"/></svg>
    <span>317-555-0192</span>
  </div>
</section>

<footer class="site-footer">
  <div class="footer-brand">Dean Morley</div>
  <nav class="footer-nav">
    <a href="#" style="left:347px">HOME</a>
    <a href="#" style="left:541px">ABOUT US</a>
    <a href="#" style="left:748px">CONTACT US</a>
  </nav>
  <div class="footer-sep" style="left:471px"></div>
  <div class="footer-sep" style="left:679px"></div>
  <p class="copyright">Copyright &nbsp;@ &nbsp;2023 All rights reserved</p>
  <div class="social" aria-label="Social links"><span></span><span></span><span></span><span></span></div>
</footer>

</body>
</html>
```